We need an attractive business card design that is modern and inviting. We like the blue and yellow (or gold) colors that are displayed with the logo. The business should communicate trust, experience, and integrity.

Target Market(s)

Residential and Commercial

Industry/Entity Type

Business

Contact Information for Business Card

Recessed Lighting
LED Retro Fit
Sign Repair
Alarms and Cameras
Mobile Home Services
24hr service calls

Font styles to use
Serif
Sans Serif

Colors
3176b5
0455a3
fece3e
fbee3e

Requirements
Must have
• Brondle Electric
• Owner: Marcus Tivane
• Licensed and Insured
• TECL #58917
Nice to have
• Exquisite Detail!!
• Over 20 years of experience
Should not have
• Nothing boring or traditional!!!

```html
<!DOCTYPE html>
<html lang="en">
<head>
<meta charset="utf-8">
<title>Brondle Electric – Business Card</title>
<link href="https://fonts.googleapis.com/css2?family=Open+Sans:wght@400;600;700&display=swap" rel="stylesheet">
<style>
  :root {
    --yellow: #f7ef2a;
    --gold: #fbee3e;
    --blue: #0455a3;
    --blue-light: #3176b5;
    --ink: #1f1f1f;
    --black: #0d0d0d;
    --white: #ffffff;
    --grey: #d6d6d6;
    --bg: #ececec;
  }
  * { box-sizing: border-box; margin: 0; padding: 0; }
  html, body { width: 1200px; height: 900px; overflow: hidden; }
  body {
    background: var(--bg);
    font-family: "Open Sans", Arial, sans-serif;
    display: flex;
    align-items: center;
    justify-content: center;
    gap: 40px;
  }
  .card {
    width: 540px;
    height: 310px;
    position: relative;
    box-shadow: 0 6px 18px rgba(0,0,0,0.18);
  }

  /* Front */
  .card-front {
    background: var(--yellow);
    display: flex;
    flex-direction: column;
    align-items: center;
    padding-top: 58px;
  }
  .brand {
    display: flex;
    align-items: center;
    gap: 14px;
  }
  .brand-dot {
    width: 44px; height: 44px;
    border: 5px solid var(--blue);
    border-radius: 50%;
  }
  .brand-name {
    font-weight: 700;
    font-size: 38px;
    letter-spacing: 1px;
    text-transform: uppercase;
    color: var(--blue);
  }
  .services {
    margin-top: 38px;
    list-style: none;
    display: flex;
    flex-wrap: wrap;
    justify-content: center;
    column-gap: 18px;
    row-gap: 4px;
    width: 430px;
    font-size: 15px;
    color: var(--ink);
  }
  .services li { display: flex; align-items: center; gap: 6px; }
  .services li.plain::before { display: none; }
  .services li::before {
    content: "";
    width: 9px; height: 9px;
    border-radius: 50%;
    background: var(--blue-light);
    border: 2px solid var(--blue);
  }

  /* Back */
  .card-back {
    background: var(--black);
    color: var(--white);
  }
  .back-brand {
    position: absolute;
    left: 40px; top: 100px;
    width: 230px;
    display: flex;
    flex-direction: column;
    align-items: center;
    gap: 12px;
  }
  .back-brand .brand-dot { width: 62px; height: 62px; border-width: 7px; }
  .back-brand .brand-name { font-size: 26px; color: var(--blue-light); text-align: center; line-height: 1.15; }
  .divider {
    position: absolute;
    left: 300px; top: 48px;
    width: 1px; height: 150px;
    background: var(--gold);
  }
  .contact {
    position: absolute;
    left: 326px; top: 52px;
    font-size: 13px;
    line-height: 1.35;
    color: var(--grey);
  }
  .contact .owner-name {
    font-weight: 700;
    font-size: 16px;
    color: var(--gold);
    text-transform: uppercase;
  }
  .contact .role { margin: 0 0 8px 14px; }
  .contact .cred { margin-left: 30px; margin-bottom: 10px; }
  .contact .line { display: flex; align-items: center; gap: 6px; margin-left: 30px; color: var(--white); }
  .contact svg { width: 11px; height: 11px; fill: var(--gold); }
  .experience {
    position: absolute;
    left: 0; right: 0; bottom: 40px;
    text-align: center;
    font-weight: 600;
    font-size: 21px;
    letter-spacing: 0.5px;
    color: var(--gold);
    text-transform: uppercase;
  }
</style>
</head>
<body>
  <section class="card card-front">
    <div class="brand">
      <span class="brand-dot"></span>
      <span class="brand-name">Brondle Electric</span>
    </div>
    <ul class="services">
      <li>Residential and Commercial</li>
      <li>Recessed Lighting</li>
      <li class="plain">LED Retro Fit</li>
      <li>Sign Repair</li>
      <li>Alarms and Cameras</li>
      <li class="plain">Mobile Home Services</li>
      <li>24hr service calls</li>
    </ul>
  </section>

  <section class="card card-back">
    <div class="back-brand">
      <span class="brand-dot"></span>
      <span class="brand-name">Brondle Electric</span>
    </div>
    <div class="divider"></div>
    <div class="contact">
      <div class="owner-name">Marcus Tivane</div>
      <div class="role">Owner</div>
      <div class="cred">Licensed &amp; Insured<br>TECL #58917</div>
      <div class="line">
        <svg viewBox="0 0 24 24" aria-hidden="true"><path d="M6.6 10.8a15 15 0 0 0 6.6 6.6l2.2-2.2a1 1 0 0 1 1-.25 11.4 11.4 0 0 0 3.6.57 1 1 0 0 1 1 1V20a1 1 0 0 1-1 1A17 17 0 0 1 3 4a1 1 0 0 1 1-1h3.5a1 1 0 0 1 1 1c0 1.25.2 2.45.57 3.57a1 1 0 0 1-.25 1z"/></svg>
        14385920
      </div>
      <div class="line">
        <svg viewBox="0 0 24 24" aria-hidden="true"><path d="M2 5h20v14H2zm2 2v.5l8 5 8-5V7l-8 5z"/></svg>
        info@brondle.com
      </div>
    </div>
    <div class="experience">Over 20 years of experience</div>
  </section>
</body>
</html>
```